Web Design Project

I need designs (PSD only - no programming) for several pages of a new website helping train operators to manage key information about their traindrivers.
The main feature of this website is the management of personnel records (create, edit, search, delete). Another key aspect is the management of user privileges. Since this is a new website we also need a user friendly frontpage, pricing information and how it works sections.
This can be broken down into 9 pages for which we need designs (PSDs).
1. Home
2. Driver record
3. How it works
4. Pricing
5. User administration
6. Help
7. Record list view
8. Login
9. Registration
Navigation (not logged in) are: Home | How it works | Pricing | Customers | About us | Contact
Navigation (logged in) are: Overview | Administration | Manage records | Billing | Help | Contact
Footer: Customer logos | Awards | Terms & Conditions | Privacy
To provide the best support for you to come up with a strong design proposal I will provide DAILY feedback to all participants. We have also created concept mockups (attached) and example pages (below) for each section to give you a clear sense of what we look for.
The core concepts for a successful bid are that the website is EASY to understand, INTUITIVE to navigate, and SIMPLE to use. Most of our users lack technical background and are looking for tool to simplify their work.
The strongest participants (winner and close contenders) will have the opportunity to additional commissioned work on additional sections not included in this brief.
Example Pages (by section)
1. http://www.quorvane.example/site-keepers/
1. http://www.vrm.example/
1. http://www.tovasko.example/
1. http://www.glimmerhootz.example/
2. http://www.pendlo.example/profile_edit.gne
3. https://www.drav.example/how-it-works/
3. http://www.wexalot.example/learn
4. http://www.brindlequay.example/crm/editions-pricing.jsp
4. http://www.quorvane.example/site-keepers/rates
6. https://support.zoltu.example/en-gb/
6. http://help.harbenquill.example/contact_us
8. https://www.morvelnet.example/uas/login
8. https://www.harbenquill.example/login
8. http://www.ublix.example/login/index
For form designs we like Ferrowen, Okvo, Pendlo, Morvelnet, Trellimap and the concepts presented by Dario Fenstermack in his classic Panel Craft Beyond the Checkboxes.
For additional guidance see mockups attached!
Target Market(s)
Security, human resources and admin support employees for train operators.
Industry/Entity Type
Learn
Requirements
Should not have
- Home page should not have
Social media icons (trellimap, pellomb, Morvelnet, RSS feed)
Contact forms
Read more links
Old trains

```html
<!DOCTYPE html>
<html lang="en">
<head>
<meta charset="utf-8">
<title>RailRosta – Manage your drivers</title>
<link href="https://fonts.googleapis.com/css2?family=Arimo:wght@400;700&display=swap" rel="stylesheet">
<style>
:root{
  --topbar:#1f3556;
  --topbar-dark:#14243d;
  --nav-text:#555;
  --nav-active:#000;
  --divider:#bbb;
  --accent:#f7a800;
  --accent-light:#ffc21a;
  --benefit-title:#a0a0a0;
  --body-text:#222;
  --blue:#0a64b0;
  --blue-dark:#07529a;
  --green:#6ea84c;
  --logo-bg-top:#c6c6c6;
  --logo-bg-bottom:#a9a9a9;
  --logo-text:#7a6969;
  --white:#fff;
}
*{margin:0;padding:0;box-sizing:border-box}
html,body{width:1150px;height:1200px;overflow:hidden}
body{position:relative;font-family:"Arimo",Arial,sans-serif;background:var(--white);color:var(--body-text)}
.abs{position:absolute}

.topbar{left:0;top:0;width:1150px;height:44px;background:linear-gradient(var(--topbar),var(--topbar-dark))}
.account-links{left:894px;top:14px;font-size:12px;color:#b9c4d4;letter-spacing:.2px}
.account-links span{margin:0 5px}
.lang{left:994px;top:16px;width:22px;height:12px;background:#2a3f86;border:1px solid #d9dde6}

.mainnav{left:0;top:44px;width:1150px;height:34px;background:var(--white);border-bottom:1px solid #ddd}
.mainnav a{position:absolute;top:10px;font-size:14.5px;color:var(--nav-text);text-decoration:none}
.mainnav a.active{color:var(--nav-active)}
.mainnav i{position:absolute;top:10px;width:1px;height:16px;background:var(--divider)}

.hero{left:0;top:78px;width:1150px;height:336px;overflow:hidden}
.hero-photo{left:0;top:0;width:771px;height:336px;background:linear-gradient(100deg,#6a5c3a 0%,#e6a614 18%,#f2b51a 45%,#c98f12 70%,#3a3a3a 88%,#9a8f80 100%)}
.hero-panel{left:771px;top:0;width:379px;height:336px;background:radial-gradient(ellipse at 60% 40%,#b9ab98 0%,#8f7c65 55%,#5c4a38 100%);border-left:1px solid #d8cfc2}
.hero-title{left:823px;top:47px;color:var(--white);font-weight:700;font-size:28px;line-height:25px;white-space:nowrap;text-shadow:1px 2px 3px rgba(0,0,0,.55)}
.hero-title .l2{display:block;padding-left:25px}
.hero-points{left:792px;top:143px;list-style:none;color:var(--white);font-weight:700;font-size:14px;white-space:nowrap;text-shadow:1px 1px 2px rgba(0,0,0,.5)}
.hero-points li{position:relative;padding-left:22px;height:28px}
.hero-points li::before{content:"";position:absolute;left:0;top:4px;width:10px;height:10px;border-radius:50%;background:#d7d3cc}
.cta{left:849px;top:211px;width:250px;height:42px;border-radius:4px;background:linear-gradient(var(--accent-light),var(--accent));color:var(--white);font-weight:700;font-size:19px;text-align:center;line-height:42px;box-shadow:0 2px 4px rgba(0,0,0,.3)}
.dots{left:523px;top:317px}
.dots span{position:absolute;top:0;width:11px;height:11px;border-radius:50%;background:#777;border:1px solid #ddd}
.dots span.on{background:#1a6fc7}

.benefits-title{left:0;top:421px;width:1150px;text-align:center;font-size:19px;color:#555}
.benefits-rule{left:119px;top:443px;width:910px;height:1px;background:#ccc}
.benefit{width:380px;height:60px}
.benefit svg{position:absolute;left:0;top:0}
.benefit h3{position:absolute;left:62px;top:0;font-weight:400;font-size:20px;color:var(--benefit-title)}
.benefit p{position:absolute;left:62px;top:27px;font-size:11px;line-height:12.5px;color:var(--body-text)}

.howto{left:0;top:723px;width:1150px;height:252px;background:linear-gradient(var(--blue),var(--blue-dark))}
.howto-title{left:0;top:6px;width:1150px;text-align:center;color:var(--white);font-size:26px;font-weight:400}
.howto-rule{left:144px;top:40px;width:907px;height:1px;background:#7fb0de}
.row-letter{left:121px;color:var(--white);font-size:32px}
.step{color:var(--white);font-size:21.5px;text-shadow:1px 1px 2px rgba(0,0,0,.35);white-space:nowrap}
.save{color:var(--white);font-size:24px;white-space:nowrap}
.num{width:34px;height:34px}

.logo-field{left:0;top:975px;width:1150px;height:184px;background:linear-gradient(var(--logo-bg-top),var(--logo-bg-bottom))}
.logo-field span{position:absolute;left:0;top:38px;width:1150px;text-align:center;font-size:92px;color:var(--logo-text);letter-spacing:1px}

.footer{left:0;top:1159px;width:1150px;height:41px;background:var(--blue);color:var(--white);font-size:18px;text-align:center;line-height:41px}
</style>
</head>
<body>

<header class="abs topbar">
  <div class="abs account-links">Sign up<span>|</span>Login<span>|</span></div>
  <div class="abs lang" aria-label="Language: English"></div>
</header>

<nav class="abs mainnav">
  <a class="active" style="left:233px">HOME</a>
  <i style="left:294px"></i>
  <a style="left:312px">HOW IT WORKS</a>
  <i style="left:444px"></i>
  <a style="left:469px">PRICES</a>
  <i style="left:543px"></i>
  <a style="left:561px">OUR CUSTOMERS</a>
  <i style="left:709px"></i>
  <a style="left:729px">ABOUT US</a>
  <i style="left:831px"></i>
  <a style="left:851px">CONTACT</a>
</nav>

<section class="abs hero">
  <div class="abs hero-photo" role="img" aria-label="Photo of a modern yellow tram in motion overlaid with faint data labels"></div>
  <div class="abs hero-panel"></div>
  <h1 class="abs hero-title">Manage your drivers<span class="l2">and key information!</span></h1>
  <ul class="abs hero-points">
    <li>Store, edit , delete and manage your drivers!</li>
    <li>Ultimate management and user privilages</li>
  </ul>
  <div class="abs cta">Sign up or Request a call</div>
  <div class="abs dots">
    <span style="left:0"></span><span class="on" style="left:30px"></span><span style="left:60px"></span><span style="left:91px"></span>
  </div>
</section>

<div class="abs benefits-title">The Benifits</div>
<div class="abs benefits-rule"></div>

<svg width="0" height="0" style="position:absolute">
  <defs>
    <radialGradient id="iconGrad" cx="40%" cy="35%" r="65%">
      <stop offset="0" stop-color="#e6e6e6"/><stop offset="1" stop-color="#9a9a9a"/>
    </radialGradient>
  </defs>
</svg>

<div class="abs benefit" style="left:216px;top:468px">
  <svg width="52" height="52"><circle cx="26" cy="26" r="25" fill="url(#iconGrad)" stroke="#ccc"/><rect x="16" y="24" width="6" height="13" fill="#fff"/><path d="M23 24 L28 14 Q31 14 30 20 L35 20 Q38 21 36 25 L35 36 L23 36 Z" fill="#fff"/></svg>
  <h3>Ease of use</h3>
  <p>Help text, reminders of important dates and events,</p>
</div>
<div class="abs benefit" style="left:663px;top:468px">
  <svg width="52" height="52"><circle cx="26" cy="26" r="25" fill="url(#iconGrad)" stroke="#ccc"/><path d="M15 26 L23 34 L39 15" fill="none" stroke="#f5a400" stroke-width="5" stroke-linecap="round"/></svg>
  <h3>EU Compliant</h3>
  <p>Follows the latest directives</p>
</div>
<div class="abs benefit" style="left:216px;top:548px">
  <svg width="52" height="52"><circle cx="26" cy="26" r="25" fill="url(#iconGrad)" stroke="#ccc"/><path d="M20 24 V19 A6 6 0 0 1 32 19 V24" fill="none" stroke="#fff" stroke-width="3"/><rect x="17" y="24" width="18" height="14" rx="2" fill="#fff"/><circle cx="26" cy="30" r="2" fill="#999"/></svg>
  <h3>Safe</h3>
  <p>Securely stored in the cloud</p>
</div>
<div class="abs benefit" style="left:663px;top:548px">
  <svg width="52" height="52"><circle cx="26" cy="26" r="25" fill="url(#iconGrad)" stroke="#ccc"/><path d="M18 36 L23 28 L28 32 L31 22 M22 22 L30 20 L36 25" fill="none" stroke="#fff" stroke-width="3" stroke-linecap="round"/><circle cx="33" cy="15" r="3" fill="#fff"/></svg>
  <h3>Fast</h3>
  <p>Pre-filled fields, logical structure, smart categories,<br>one-click PDF generation</p>
</div>
<div class="abs benefit" style="left:216px;top:628px">
  <svg width="52" height="52"><circle cx="26" cy="26" r="25" fill="url(#iconGrad)" stroke="#ccc"/><g fill="none" stroke="#fff" stroke-width="1.8"><circle cx="26" cy="26" r="13"/><ellipse cx="26" cy="26" rx="6" ry="13"/><line x1="13" y1="26" x2="39" y2="26"/><line x1="15" y1="19" x2="37" y2="19"/><line x1="15" y1="33" x2="37" y2="33"/></g></svg>
  <h3>Accessible</h3>
  <p>Storage allow easy access from anywhere and privilege<br>&nbsp;rights &nbsp;across &nbsp;different users &nbsp;allows collaborative work</p>
</div>

<section class="abs howto">
  <h2 class="abs howto-title">How it works</h2>
  <div class="abs howto-rule"></div>

  <div class="abs row-letter" style="top:52px">A...</div>
  <svg class="abs num" style="left:208px;top:56px"><circle cx="17" cy="17" r="16" fill="#fff"/><text x="17" y="25" text-anchor="middle" font-size="22" font-weight="700" fill="#6ea84c" font-family="Arimo,sans-serif">1</text></svg>
  <div class="abs step" style="left:251px;top:60px">Register a driver</div>
  <svg class="abs num" style="left:441px;top:56px"><circle cx="17" cy="17" r="16" fill="#fff"/><text x="17" y="25" text-anchor="middle" font-size="22" font-weight="700" fill="#6ea84c" font-family="Arimo,sans-serif">2</text></svg>
  <div class="abs step" style="left:485px;top:60px">Click new certificate</div>
  <svg class="abs num" style="left:712px;top:56px"><circle cx="17" cy="17" r="16" fill="#fff"/><text x="17" y="25" text-anchor="middle" font-size="22" font-weight="700" fill="#6ea84c" font-family="Arimo,sans-serif">3</text></svg>
  <div class="abs step" style="left:760px;top:60px">Register information</div>
  <div class="abs save" style="left:967px;top:59px">&gt;&gt; Save</div>

  <div class="abs row-letter" style="top:117px">B...</div>
  <svg class="abs num" style="left:208px;top:121px"><circle cx="17" cy="17" r="16" fill="#fff"/><text x="17" y="25" text-anchor="middle" font-size="22" font-weight="700" fill="#6ea84c" font-family="Arimo,sans-serif">1</text></svg>
  <div class="abs step" style="left:251px;top:125px">Register an update</div>
  <svg class="abs" style="left:443px;top:113px" width="76" height="72"><line x1="8" y1="64" x2="32" y2="40" stroke="#fff" stroke-width="6" stroke-linecap="round"/><circle cx="49" cy="24" r="19" fill="#0a64b0" stroke="#fff" stroke-width="5"/><circle cx="49" cy="24" r="13" fill="#fff"/><text x="49" y="32" text-anchor="middle" font-size="20" font-weight="700" fill="#6ea84c" font-family="Arimo,sans-serif">2</text></svg>
  <div class="abs step" style="left:526px;top:125px">Search records</div>
  <svg class="abs num" style="left:712px;top:121px"><circle cx="17" cy="17" r="16" fill="#fff"/><text x="17" y="25" text-anchor="middle" font-size="22" font-weight="700" fill="#6ea84c" font-family="Arimo,sans-serif">3</text></svg>
  <div class="abs step" style="left:760px;top:126px">Update fields</div>
  <div class="abs save" style="left:904px;top:124px">&gt;&gt; Save</div>

  <div class="abs row-letter" style="top:186px">C...</div>
  <svg class="abs num" style="left:208px;top:190px"><circle cx="17" cy="17" r="16" fill="#fff"/><text x="17" y="25" text-anchor="middle" font-size="22" font-weight="700" fill="#6ea84c" font-family="Arimo,sans-serif">1</text></svg>
  <div class="abs step" style="left:250px;top:196px">Generate a certificate</div>
  <svg class="abs num" style="left:491px;top:190px"><circle cx="17" cy="17" r="16" fill="#fff"/><text x="17" y="25" text-anchor="middle" font-size="22" font-weight="700" fill="#6ea84c" font-family="Arimo,sans-serif">2</text></svg>
  <div class="abs step" style="left:534px;top:196px">Search records</div>
  <svg class="abs num" style="left:712px;top:190px"><circle cx="17" cy="17" r="16" fill="#fff"/><text x="17" y="25" text-anchor="middle" font-size="22" font-weight="700" fill="#6ea84c" font-family="Arimo,sans-serif">3</text></svg>
  <div class="abs step" style="left:762px;top:195px">Click print PDF</div>
</section>

<section class="abs logo-field"><span>LOGO FIELD</span></section>

<footer class="abs footer">Copywrite © 2012 RailRosta | All rights reserved | T&amp;C Home | How it Works | Prices | Our Customers | About Us | Contact</footer>

</body>
</html>
```